Business card design needed

I am branching out into the world of private practice in Speech Pathology. My clients will be aged 0-17; the business card will be distributed within my existing teacher and parent networks in schools.

I work with clients to develop their speech, language, literacy, fluency, swallowing and voice. I like to think that parents hand over their money to me because I've offered a fun session with positive outcomes/growth and for an affordable price.

I'm flexible with colours; though think something bright would be ideal. I'm not wanting anything too cutesy or 'little kid'. I'd like for it to stand out in a bulging purse or on a fridge crammed with papers.

Industry/Entity Type

Teacher

Contact Information for Business Card

Wren Hollow Speech Pathology Pty Ltd
Molly Fenwick
Speech Pathologist
Ph: 0419 826 307
Email: mollyfenwick@quillpost.com

Logo Text

Logo styles of interest
Character Logo
Wordmark Logo
Lettermark Logo
Requirements
Must have
• A kind of graphic to represent the core business - that is, providing intervention to children 0-17 with communication needs (e.g., speech, language, literacy, swallowing, voice, fluency)

Should not have
• Pictures of babies or children.
Love hearts.

```html
<!DOCTYPE html>
<html lang="en">
<head>
<meta charset="utf-8">
<title>Wren Hollow Speech Pathology – Business Card</title>
<link rel="stylesheet" href="https://fonts.googleapis.com/css2?family=Didact+Gothic&family=Open+Sans:ital,wght@0,400;0,700;1,400&display=swap">
<style>
  :root {
    --page-bg: #e9edf0;
    --card-blue: #2ab4ee;
    --card-blue-light: #5fcbf5;
    --card-blue-deep: #1a9fdc;
    --ink-white: #ffffff;
    --ink-navy: #0f2d47;
  }
  * { box-sizing: border-box; margin: 0; padding: 0; }
  html, body {
    width: 1200px;
    height: 849px;
    overflow: hidden;
    background: var(--page-bg);
  }
  .stage {
    width: 1200px;
    height: 849px;
    display: flex;
    align-items: center;
    justify-content: center;
  }
  .business-card {
    position: relative;
    width: 1000px;
    height: 606px;
    background: linear-gradient(135deg, var(--card-blue-light) 0%, var(--card-blue) 45%, var(--card-blue-deep) 100%);
    box-shadow: 0 10px 30px rgba(0, 0, 0, 0.18);
    overflow: hidden;
    font-family: "Open Sans", sans-serif;
  }
  .identity {
    position: absolute;
    left: 62px;
    top: 82px;
    width: 400px;
  }
  .person-name {
    font-family: "Didact Gothic", sans-serif;
    font-weight: 400;
    font-size: 52px;
    letter-spacing: 1px;
    color: var(--ink-navy);
    line-height: 1.1;
  }
  .person-role {
    margin-top: 10px;
    font-weight: 700;
    font-size: 22px;
    color: var(--ink-white);
  }
  .divider {
    margin-top: 12px;
    width: 395px;
    height: 4px;
    background: var(--ink-white);
  }
  .contact-list {
    list-style: none;
    margin-top: 32px;
  }
  .contact-item {
    display: flex;
    align-items: center;
    gap: 22px;
    margin-bottom: 20px;
    font-size: 26px;
    color: var(--ink-navy);
  }
  .contact-icon {
    width: 26px;
    height: 26px;
    flex: none;
  }
  .brand {
    position: absolute;
    left: 560px;
    top: 120px;
    width: 400px;
    display: flex;
    align-items: center;
    gap: 22px;
  }
  .brand-dot {
    width: 44px;
    height: 44px;
    border-radius: 50%;
    background: var(--ink-white);
    flex: none;
  }
  .brand-name {
    font-family: "Didact Gothic", sans-serif;
    font-weight: 400;
    font-size: 36px;
    line-height: 1.15;
    color: var(--ink-navy);
  }
  .mission {
    position: absolute;
    left: 455px;
    top: 430px;
    width: 500px;
    font-size: 19px;
    line-height: 1.45;
    color: var(--ink-navy);
  }
  .quote-mark {
    font-family: Georgia, serif;
    font-weight: 700;
    font-size: 44px;
    line-height: 0;
    color: var(--ink-navy);
  }
  .quote-open { margin-right: 6px; vertical-align: -14px; }
  .quote-close { margin-left: 8px; vertical-align: -22px; }
</style>
</head>
<body>
<main class="stage">
  <article class="business-card">
    <section class="identity">
      <h1 class="person-name">Molly Fenwick</h1>
      <p class="person-role">Speech Pathologist</p>
      <div class="divider"></div>
      <ul class="contact-list">
        <li class="contact-item">
          <svg class="contact-icon" viewBox="0 0 24 24" aria-hidden="true">
            <path fill="#ffffff" d="M6.6 10.8a15.2 15.2 0 0 0 6.6 6.6l2.2-2.2a1 1 0 0 1 1-.25 11.4 11.4 0 0 0 3.6.57 1 1 0 0 1 1 1V20a1 1 0 0 1-1 1A17 17 0 0 1 3 4a1 1 0 0 1 1-1h3.5a1 1 0 0 1 1 1c0 1.25.2 2.46.57 3.6a1 1 0 0 1-.25 1z"/>
          </svg>
          <span>0419 826 307</span>
        </li>
        <li class="contact-item">
          <svg class="contact-icon" viewBox="0 0 24 24" aria-hidden="true">
            <rect x="2" y="5" width="20" height="14" fill="#ffffff"/>
            <path d="M2 5l10 8 10-8" fill="none" stroke="#2ab4ee" stroke-width="2"/>
          </svg>
          <span>mollyfenwick@quillpost.com</span>
        </li>
      </ul>
    </section>

    <div class="brand">
      <span class="brand-dot"></span>
      <p class="brand-name">Wren Hollow<br>Speech Pathology<br>Pty Ltd</p>
    </div>

    <p class="mission">
      <span class="quote-mark quote-open">&ldquo;</span>Providing fun, effective and affordable intervention to support developments of speech and language skills in children and adolescents.<span class="quote-mark quote-close">&rdquo;</span>
    </p>
  </article>
</main>
</body>
</html>
```